Purchasing Management Consulting B to B Web Design PAYMENT GUARANTY

We'd like to build a new digital image for our website.

Our company is managing purchasing consultancy services for Large and Medium companies around 4 activities :
- Procurement outsourcing
- Purchasing consulting (cost reduction)
- Supply chain training
- Web platform to manage Supplier risk (TrovaNorm.com)

We now aim to harmonies our website in term of design in order to build a strongest Corporate Image.

SEE REQUIREMENT ENCLOSED

Please have a look on our current websites:
- www.kelpstrand.com
- www.qtr-network.com
- www.trovanorm.com

Reason: Hello, Some project received are not really professional and need more details. I did not see all deliverable requested in specifications. I'll revert to designer to improve design. Regards, Gaspard

Reason: Only few designers reply and feedback still need to be done.

Target Market(s)

Our business is exclusively Business to Business toward Medium and Large companies.

Industry/Entity Type

Digital

Requirements
Must have
• Website will be developped in Joomla CMS.
The user community will use Jomsocial module : Visitor should be "influenced" to communicate its contact details by registering the community.

Ergonomy, Simplicity and professionnalism is the key objectives.

Deliverables :
- Corporate Home page including clear access to our 4 activities
- Dynamique banner
- Corporate article / contact pages (1 or 2)
- Activities home pages (x 4)
- Activity Catalog (Indesign for paper version)
Nice to have
• Integration of Design for our consulting and training catalog will be interesting.

Livechat design (the one of Pixelharbor.com is good)
Should not have
• Only psd

Not html

```html
<!DOCTYPE html>
<html lang="fr">
<head>
<meta charset="utf-8">
<title>Kelp Strand – Achetez en toute simplicite</title>
<link href="https://fonts.googleapis.com/css2?family=Source+Sans+3:wght@300;400;600&display=swap" rel="stylesheet">
<style>
:root{
  --gold:#e9b92f;
  --gold-soft:#f2d07a;
  --nav-gold:#edb834;
  --nav-text:#7a2d00;
  --heading:#86701c;
  --brand:#8a6a12;
  --text:#3a3a3a;
  --panel:#f5f6fa;
  --footer:#eeeeee;
}
*{box-sizing:border-box;margin:0;padding:0}
html,body{width:1200px;height:891px;overflow:hidden}
body{position:relative;font-family:"Source Sans 3",Arial,sans-serif;color:var(--text);background:#fff}
.abs{position:absolute}

.header{left:0;top:0;width:1200px;height:105px;background:linear-gradient(180deg,#f1f1f1,#e6e6e6)}
.brand-name{left:168px;top:34px;font-size:25px;font-weight:600;color:var(--brand);white-space:nowrap}
.language{left:889px;top:14px;width:150px;height:27px;background:#fff;border:1px solid #bbb;border-radius:3px;font-size:11px;color:#555;padding:6px 7px}
.language svg{position:absolute;right:8px;top:11px}
.nav{left:514px;top:56px;height:38px;display:flex;background:var(--nav-gold);box-shadow:0 2px 3px rgba(0,0,0,.25);border-radius:2px}
.nav a{display:block;text-align:center;line-height:38px;font-size:13px;color:var(--nav-text);text-decoration:none;border-right:1px solid #c9951d}
.nav a:last-child{border-right:none}

.login{left:0;top:105px;width:1200px;height:45px;background:#fff}
.login label{position:absolute;top:13px;font-size:12px;color:#444}
.login .field{position:absolute;top:9px;width:142px;height:26px;border:1px solid #d0d0d0;background:#fff}
.btn{background:var(--gold);color:#333;font-size:13px;text-align:center;border:1px solid #d7a72a}

.activities{left:0;top:150px;width:1200px;height:161px;background:var(--gold-soft)}
.activities h1{position:absolute;top:18px;width:100%;text-align:center;font-weight:300;font-size:29px;color:#5a4a1a}
.activity{position:absolute;top:76px;width:110px;text-align:center;font-size:14px;color:#4a3d10}
.activity .icon{display:block;width:40px;height:40px;margin:0 auto 10px;border-radius:6px}

.banner{left:0;top:311px;width:1200px;height:296px;background:var(--gold);border-top:1px solid #f3d98a}
.slide{left:166px;top:9px;width:868px;height:282px;background:var(--panel)}
.slide-photo{left:0;top:0;width:524px;height:282px;background:linear-gradient(120deg,#6c6f78 0%,#b3aa9c 40%,#e9e6e2 75%,#f7f7f7 100%)}
.slide h2{left:547px;top:37px;font-weight:300;font-size:29px;color:var(--heading)}
.slide p{left:551px;top:81px;width:296px;font-size:12.5px;line-height:22px;color:#333}
.dots{left:554px;top:248px;display:flex;gap:6px}
.dots span{width:12px;height:12px;border-radius:50%;background:#c8c8c8}
.dots span.on{background:var(--gold)}

.col h3{position:absolute;font-weight:300;font-size:25px;color:var(--heading)}
.col p{position:absolute;font-size:12px;line-height:18.5px;color:#333}
.news-photo{left:169px;top:667px;width:206px;height:107px;background:linear-gradient(100deg,#2f3440,#8a8f99 55%,#e6e6e6)}
.badge{left:608px;top:678px;width:192px;height:87px;border-radius:6px;background:linear-gradient(180deg,#fafafa 0 55%,#f07b1d 55% 100%);box-shadow:0 2px 4px rgba(0,0,0,.25)}
.news label{position:absolute;left:830px;top:669px;font-size:12px;color:#666}
.news .field{position:absolute;left:831px;top:686px;width:204px;height:26px;border:1px solid #bbb;background:#fff}
.social{left:866px;top:776px;display:flex;gap:9px}
.social span{width:28px;height:28px;border-radius:4px}

.footer{left:0;top:838px;width:1200px;height:53px;background:var(--footer)}
.footer nav{position:absolute;top:20px;width:100%;text-align:center;font-size:12px;color:#333}
.footer nav span{margin:0 7px;color:#666}
</style>
</head>
<body>

<header class="abs header">
  <div class="abs brand-name">Kelp Strand</div>
  <div class="abs language">Language
    <svg width="10" height="6" viewBox="0 0 10 6"><path d="M0 0h10L5 6z" fill="#444"/></svg>
  </div>
  <nav class="abs nav">
    <a href="#" style="width:89px">ACCUEIL</a><a href="#" style="width:120px">KELP STRAND</a><a href="#" style="width:88px">METIERS</a><a href="#" style="width:130px">NOS REFERENCES</a><a href="#" style="width:98px">CONTACT</a>
  </nav>
</header>

<section class="abs login">
  <label style="left:564px">Utilisateur</label>
  <div class="field" style="left:620px"></div>
  <label style="left:775px">Mot de Passe</label>
  <div class="field" style="left:845px"></div>
  <div class="abs btn" style="left:997px;top:9px;width:43px;height:26px;line-height:24px">OK</div>
</section>

<section class="abs activities">
  <h1>Achetez en toute simplicite</h1>
  <div class="activity" style="left:345px"><span class="icon" role="img" aria-label="Icône communauté" style="background:#c9822a"></span>Communaute</div>
  <div class="activity" style="left:456px"><span class="icon" role="img" aria-label="Icône consulting" style="background:#6f8a9a"></span>Cosnulting</div>
  <div class="activity" style="left:558px"><span class="icon" role="img" aria-label="Icône formation" style="background:#3f7a5a"></span>Formation</div>
  <div class="activity" style="left:653px"><span class="icon" role="img" aria-label="Icône graphique TrovaNorm" style="background:#d9883a"></span>TrovaNorm</div>
  <div class="activity" style="left:750px"><span class="icon" role="img" aria-label="Icône multi devis" style="background:#6f8a9a"></span>Multi Devis</div>
</section>

<section class="abs banner">
  <div class="abs slide">
    <div class="abs slide-photo" role="img" aria-label="Photo d'une équipe d'affaires en réunion autour d'un ordinateur portable"></div>
    <h2 class="abs">Welcome to our site</h2>
    <p class="abs">Lorem Ipsum is simply dummy text of the printing and typesetting industry. Lorem Ipsum has been the industry's standard dummy text ever since the 1500s, when an unknown printer took a galley of type and scrambled it to make a type specimen book.</p>
    <div class="abs dots"><span></span><span class="on"></span><span></span><span></span><span></span></div>
  </div>
</section>

<section class="col">
  <h3 style="left:170px;top:624px">Actualites</h3>
  <div class="abs news-photo" role="img" aria-label="Photo d'un homme d'affaires lisant un journal"></div>
  <p style="left:168px;top:782px;width:210px">Lorem Ipsum is simply dummy text of the printing and typesetting industry</p>

  <h3 style="left:388px;top:624px">Kelp Strand</h3>
  <p style="left:388px;top:666px;width:206px;text-align:justify">Lorem Ipsum is simply dummy text of the printing and typesetting industry. Lorem Ipsum has been the industry's standard dummy text ever since the 1500s, when an unknown printer took a galley of type and scrambled it to make a type specimen book.</p>

  <h3 style="left:607px;top:624px">Nos References</h3>
  <div class="abs badge" role="img" aria-label="Badge partenaire"></div>
  <p style="left:613px;top:782px;width:200px">Lorem Ipsum is simply dummy text of printing and typesetting industry</p>
</section>

<section class="col news">
  <h3 style="left:829px;top:628px">Newsletters</h3>
  <label>Enter the Name</label>
  <div class="field"></div>
  <div class="abs btn" style="left:998px;top:716px;width:37px;height:27px;line-height:26px;font-size:12px">OK</div>
  <div class="abs social" aria-label="Réseaux sociaux">
    <span style="background:#3b5a9a"></span><span style="background:#4aa8d8"></span><span style="background:#e8821e"></span><span style="background:#1d6fa5"></span>
  </div>
</section>

<footer class="abs footer">
  <nav>Kelp Strand<span>/</span> Recrutment<span>/</span>Presse<span>/</span>Mentions Legales<span>/</span>Nous Contacter</nav>
</footer>

</body>
</html>
```